Coralith Partners's New Branding
Anything the customer sees, we want to update
Coralith Partners's New Branding -
Creative Brief
Professional
Dorian Pelk, MCP
Director of Technology
418 West Alder Road, Fenwick Vale
dorian.pelk@coralithpt.example
www.coralithpt.example
In addition to branding our business cards, we're also looking to brand: 1) folders - two pockets w/ a slotted area on the left pocket to insert a business card 2) brochures - 8.5"x11" tri-fold brochure 3) letterhead 4) envelopes 5) sales proposal cover letter - Our logo and name - Presented to: "Customer's name" - Presented by: "our sales person(s)" - Title of presentation - our web address 6) powerpoint 7) binders (including spline) 8) cd label - Company's name we're presenting cd to - our logo and name - title of content on cd
Quote: "Our business is sustaining yours" Please layout the quote so that if we put a QR code on the back of the card in the future, it won't look out of place.

```html
<!DOCTYPE html>
<html lang="en">
<head>
<meta charset="utf-8">
<title>Coralith Partners Stationery</title>
<link href="https://fonts.googleapis.com/css2?family=Cinzel:wght@600&family=Open+Sans:wght@400;600&display=swap" rel="stylesheet">
<style>
  :root {
    --bg: #efece6;
    --paper: #ffffff;
    --green-dark: #0c3f26;
    --green-mid: #1a6a3f;
    --green-text: #5aa42c;
    --ink: #1f2a24;
    --muted: #7b837e;
    --flap-ink: #cfe6cf;
    --globe-a: #eef0ef;
    --globe-b: #dde1de;
  }
  * { box-sizing: border-box; margin: 0; padding: 0; }
  html, body { width: 1200px; height: 869px; overflow: hidden; }
  body { background: var(--bg); font-family: "Open Sans", sans-serif; position: relative; }
  .piece { position: absolute; background: var(--paper); box-shadow: 0 2px 6px rgba(0,0,0,.18); overflow: hidden; }
  .flap { position: absolute; left: 0; right: 0; top: 0; background: linear-gradient(180deg, var(--green-mid), var(--green-dark)); }
  .flap-text { position: absolute; color: var(--flap-ink); font-size: 6px; letter-spacing: .5px; white-space: nowrap; }
  .brand { position: absolute; display: flex; align-items: center; gap: 6px; }
  .brand-dot { width: 16px; height: 16px; border-radius: 50%; background: var(--green-mid); flex: none; }
  .brand-name { font-family: "Cinzel", serif; font-weight: 600; color: var(--ink); font-size: 13px; letter-spacing: .5px; line-height: 1; white-space: nowrap; }
  .brand.small .brand-dot { width: 10px; height: 10px; }
  .brand.small .brand-name { font-size: 8px; }
  .globe { position: absolute; border-radius: 50%; background: radial-gradient(circle at 40% 38%, var(--globe-a), var(--globe-b)); }
  .foot { position: absolute; font-size: 5.5px; line-height: 1.45; color: var(--green-text); white-space: nowrap; }
  .foot.right { text-align: right; color: var(--muted); }

  .catalog { left: 29px; top: 78px; width: 355px; height: 697px; }
  .catalog .flap { height: 83px; border-radius: 0 0 40px 40px; }
  .letterhead { left: 425px; top: 190px; width: 309px; height: 585px; }
  .dl-back { left: 758px; top: 148px; width: 411px; height: 200px; }
  .dl-back .flap { height: 60px; clip-path: polygon(0 0,100% 0,100% 40%,50% 100%,0 40%); }
  .dl-front { left: 749px; top: 240px; width: 420px; height: 202px; }
  .card-back { left: 828px; top: 598px; width: 158px; height: 94px; border-radius: 6px; background: linear-gradient(180deg, var(--green-mid), var(--green-dark)); }
  .card-front { left: 1003px; top: 598px; width: 159px; height: 94px; border-radius: 6px; }
  .card-name { position: absolute; left: 10px; top: 34px; font-size: 6px; font-weight: 600; color: var(--ink); line-height: 1.4; }
  .card-name span { display: block; font-weight: 400; color: var(--muted); }
  .card-contact { position: absolute; left: 10px; top: 58px; font-size: 5px; line-height: 1.45; color: var(--green-text); }
</style>
</head>
<body>

<div class="piece catalog">
  <div class="flap"><div class="flap-text" style="left:110px;top:20px">Stationery for every client touchpoint</div></div>
  <div class="brand" style="left:14px;top:102px"><span class="brand-dot"></span><span class="brand-name">CORALITH PARTNERS</span></div>
  <div class="globe" role="img" aria-label="Faint globe illustration with orbit swoosh" style="left:60px;top:330px;width:230px;height:230px"></div>
  <div class="foot" style="left:14px;bottom:14px">418 West Alder Road<br>Fenwick Vale<br>www.coralithpt.example</div>
  <div class="foot right" style="right:14px;bottom:14px">Tel: 555.010.0148<br>Fax: 555.010.0149</div>
</div>

<div class="piece letterhead">
  <div class="brand" style="left:14px;top:24px"><span class="brand-dot"></span><span class="brand-name">CORALITH PARTNERS</span></div>
  <div class="globe" role="img" aria-label="Faint globe illustration with orbit swoosh" style="left:40px;top:230px;width:220px;height:220px"></div>
  <div class="foot" style="left:14px;bottom:14px">418 West Alder Road<br>Fenwick Vale<br>www.coralithpt.example</div>
  <div class="foot right" style="right:14px;bottom:14px">Tel: 555.010.0148<br>Fax: 555.010.0149</div>
</div>

<div class="piece dl-back">
  <div class="flap"><div class="flap-text" style="left:150px;top:10px">Stationery for every client touchpoint</div></div>
</div>

<div class="piece dl-front">
  <div class="brand" style="left:20px;top:20px"><span class="brand-dot"></span><span class="brand-name">CORALITH PARTNERS</span></div>
  <div class="globe" role="img" aria-label="Faint globe illustration with orbit swoosh" style="left:190px;top:30px;width:130px;height:130px"></div>
  <div class="foot" style="left:14px;bottom:12px">418 West Alder Road<br>Fenwick Vale<br>www.coralithpt.example</div>
  <div class="foot right" style="right:14px;bottom:12px">Tel: 555.010.0148<br>Fax: 555.010.0149</div>
</div>

<div class="piece card-back">
  <div class="flap-text" style="left:22px;top:44px">Stationery for every client touchpoint</div>
</div>

<div class="piece card-front">
  <div class="brand small" style="left:10px;top:10px"><span class="brand-dot"></span><span class="brand-name">CORALITH PARTNERS</span></div>
  <div class="globe" role="img" aria-label="Faint globe illustration" style="left:100px;top:26px;width:50px;height:50px"></div>
  <div class="card-name">Dorian Pelk, MCP<span>Director of Technology</span></div>
  <div class="card-contact">T 555.010.0148<br>C 555.010.0150<br>dorian.pelk@coralithpt.example</div>
</div>

</body>
</html>
```